12 Meter Banner-Design Lagerhalle
Zielgruppe
Wir errichten neue Elektroanlagen für Einfamilenhäuser und Wohnungen.
Hallo,
wir möchten auf 12 Meter drei Banner spannen um die unschönen Rohre und Kabel zu verdecken. Jeder der drei Banner soll 400cm breit und 160cm hoch werden.
-Banner 1 links: Motivationsspruch groß, mittig - : Wer immer tut, was er schon kann, bleibt immer das, was er schon ist.
- Banner 2 mitte : Komfortzone ( Grafiken habe ich im Anhang von dem Aufbau der Komfortzone ) Toll wäre ein selbst erstelltes Design passend zum Unternehmen / Farben Schriftart etc.
-Banner 3 rechts: Motivationsspruch : Zusammenkommen ist ein Beginn, zusammenbleiben ist ein Fortschritt, zusammenarbeiten ist ein Erfolg.
- Design nach Vorgabe Druckpilot ( Datasheet) erstellen
Gundsätzlich wäre super, wenn alle 3 Designs/ Banner miteinander harmonieren. Alles andere ist der Kreativität überlassen.
Schriftart: Fira Sans / Montserrat
Wir würden uns über eine Zusammenarbeit freuen.
Beste Grüße

```html
<!DOCTYPE html>
<html lang="de">
<head>
<meta charset="utf-8">
<title>Banner-Serie Lagerhalle – Brandt &amp; Keller Elektrotechnik</title>
<link rel="stylesheet" href="https://fonts.googleapis.com/css2?family=Josefin+Sans:wght@400;600;700&family=Montserrat:wght@700;800&display=swap">
<style>
  :root {
    --brand-blue: #2b9ad4;
    --brand-navy: #1d4f8f;
    --brand-orange: #f07d1c;
    --brand-teal: #3aaaa6;
    --brand-teal-light: #7cc8c3;
    --line-red: #d6262f;
    --paper: #ffffff;
    --stage: #eceff2;
    --ink: #24323f;
  }
  * { box-sizing: border-box; margin: 0; padding: 0; }
  html, body { width: 846px; height: 1200px; overflow: hidden; }
  body {
    background: var(--stage);
    font-family: "Josefin Sans", "Montserrat", sans-serif;
    display: flex;
    flex-direction: column;
    justify-content: center;
    align-items: center;
    gap: 30px;
  }
  .banner {
    position: relative;
    width: 766px;
    height: 306px;
    overflow: hidden;
    box-shadow: 0 2px 8px rgba(0,0,0,.12);
  }
  .banner--blue { background: var(--brand-blue); color: var(--paper); }
  .banner--white { background: var(--paper); color: var(--ink); }

  .quote-mark {
    position: absolute;
    font-family: "Montserrat", sans-serif;
    font-weight: 800;
    color: rgba(255,255,255,.35);
    line-height: 1;
  }
  .quote-mark--open { font-size: 210px; top: -8px; left: 36px; }
  .quote-mark--close { font-size: 130px; bottom: -62px; right: 110px; }

  .quote {
    position: absolute;
    inset: 0;
    display: flex;
    align-items: center;
    justify-content: center;
    text-align: center;
    text-transform: uppercase;
    font-weight: 600;
    letter-spacing: .04em;
  }
  .quote--large { font-size: 38px; line-height: 1.15; }

  .quote--stacked {
    justify-content: flex-start;
    text-align: left;
    padding-left: 230px;
    font-size: 25px;
    line-height: 1.3;
  }
  .quote-mark--small-open { font-size: 150px; top: 10px; left: 150px; }

  .brand {
    position: absolute;
    right: 22px;
    bottom: 16px;
    display: flex;
    align-items: center;
    gap: 6px;
    font-weight: 700;
    font-size: 11px;
    letter-spacing: .06em;
    text-transform: uppercase;
  }
  .brand__dot {
    width: 10px; height: 10px; border-radius: 50%;
    background: currentColor;
  }
  .banner--white .brand { color: var(--brand-blue); }

  .zone-chart { position: absolute; inset: 0; width: 100%; height: 100%; }
  .zone-label { font-family: "Josefin Sans", sans-serif; font-weight: 700; font-size: 7px; fill: var(--paper); text-anchor: middle; }
  .zone-note { font-family: "Josefin Sans", sans-serif; font-size: 5.5px; fill: var(--paper); }
  .vision-label { font-family: "Josefin Sans", sans-serif; font-weight: 700; font-size: 11px; fill: var(--ink); }
</style>
</head>
<body>

  <section class="banner banner--blue" aria-label="Banner links">
    <span class="quote-mark quote-mark--open">“</span>
    <p class="quote quote--large">Wer immer tut,<br>was er schon kann,<br>bleibt immer das,<br>was er schon ist.</p>
    <span class="quote-mark quote-mark--close">”</span>
    <div class="brand"><span class="brand__dot"></span>Brandt &amp; Keller</div>
  </section>

  <section class="banner banner--white" aria-label="Banner Mitte: Komfortzone">
    <svg class="zone-chart" viewBox="0 0 766 306" role="img" aria-label="Diagramm der Zonen von Komfortzone bis Vision">
      <g transform="translate(240,153) rotate(-45)">
        <rect x="0" y="0" width="198" height="198" fill="var(--brand-teal-light)" stroke="#fff" stroke-width="1.5"/>
        <rect x="0" y="0" width="150" height="150" fill="var(--brand-teal)" stroke="#fff" stroke-width="1.5"/>
        <rect x="0" y="0" width="100" height="100" fill="var(--brand-navy)" stroke="#fff" stroke-width="1.5"/>
        <rect x="0" y="0" width="50" height="50" fill="var(--brand-orange)" stroke="#fff" stroke-width="1.5"/>

        <text class="zone-note" transform="translate(73,5) rotate(90)">Ausreden suchen</text>
        <text class="zone-note" x="5" y="78">Wenig Vertrauen</text>
        <text class="zone-note" transform="translate(123,12) rotate(90)">Neues lernen</text>
        <text class="zone-note" x="12" y="127">Probleme lösen</text>
        <text class="zone-note" transform="translate(172,16) rotate(90)">Ziele erreichen</text>
        <text class="zone-note" x="16" y="176">Träume leben</text>
      </g>
      <line x1="240" y1="153" x2="600" y2="153" stroke="var(--line-red)" stroke-width="1.5"/>
      <text class="zone-label" x="276" y="150">Komfortzone</text>
      <text class="zone-label" x="346" y="150">Angstzone</text>
      <text class="zone-label" x="416" y="150">Lernzone</text>
      <text class="zone-label" x="486" y="150">Wachstumszone</text>
      <text class="vision-label" x="606" y="157">Vision</text>
    </svg>
    <div class="brand"><span class="brand__dot"></span>Brandt &amp; Keller</div>
  </section>

  <section class="banner banner--blue" aria-label="Banner rechts">
    <span class="quote-mark quote-mark--small-open">“</span>
    <p class="quote quote--stacked">Zusammenkommen<br>ist ein Beginn,<br>zusammenbleiben<br>ist ein Fortschritt,<br>zusammenarbeiten<br>ist ein Erfolg.</p>
    <div class="brand"><span class="brand__dot"></span>Brandt &amp; Keller</div>
  </section>

</body>
</html>
```